Pilates Classes Flyer Design

I need a flyer designed that will promote my range of classes held in Bath, UK. I teach beginners, intermediate level and Over 50's and 60's and also teach individuals in their own homes. I would like to see designs using my colours blue Pantone 306 and Lime Green 14-0452 TPX TCX. The flyer should reflect a friendly, welcoming and professional class structure. I attach an old flyer for your reference and copy.

Target Market(s)

Men and Women who have busy lives working hard, who recognise they need to stretch out, do some exercise and de-stress after a busy day

Ladies over 50 who want to do some Pilates in a friendly fun environment and meet people at the same time.

Industry/Entity Type

It Professional

Font styles to use
Sans Serif
Script

Requirements
Must have
• One-sided flyer
Text only logo. Drop the figure

```html
<!DOCTYPE html>
<html lang="en">
<head>
<meta charset="utf-8">
<title>Stillwater Pilates – New Classes Flyer</title>
<link rel="stylesheet" href="https://fonts.googleapis.com/css2?family=Parisienne&family=Mada:wght@300;400&family=Roboto+Condensed:wght@400&display=swap">
<style>
  :root {
    --backdrop: #a8cf56;
    --paper: #ffffff;
    --brand-blue: #29abe2;
    --brand-green: #8dc63f;
    --text-grey: #5a5a5a;
    --text-dark: #3c3c3c;
    --photo-light: #eef1f3;
    --photo-floor: #c9a77e;
    --mat-blue: #3a6fb5;
    --mat-green: #79b84a;
  }
  * { margin: 0; padding: 0; box-sizing: border-box; }
  html, body { width: 1200px; height: 1000px; overflow: hidden; }
  body { background: var(--backdrop); position: relative; font-family: "Mada", sans-serif; }

  .flyer {
    position: absolute; left: 289px; top: 57px; width: 618px; height: 885px;
    background: var(--paper); overflow: hidden;
  }
  .hero-photo {
    position: absolute; left: 30px; top: 0; width: 588px; height: 371px;
    background: linear-gradient(180deg, var(--photo-light) 0%, #f6f4f2 55%, #e3cdb2 75%, var(--photo-floor) 100%);
  }
  .title-tab {
    position: absolute; left: 69px; top: 261px; width: 211px; height: 110px;
    background: var(--paper); border-radius: 6px 6px 0 0;
  }
  .subtitle-tab {
    position: absolute; left: 69px; top: 329px; width: 426px; height: 42px;
    background: var(--paper); border-radius: 0 6px 0 0;
  }
  .title-script {
    position: absolute; left: 82px; top: 268px;
    font-family: "Parisienne", cursive; font-size: 64px; line-height: 1;
    color: var(--brand-green);
  }
  .title-sub {
    position: absolute; left: 86px; top: 338px;
    font-family: "Mada", sans-serif; font-weight: 300; font-size: 28px;
    letter-spacing: 2.6px; line-height: 1; color: var(--brand-blue);
  }
  .intro {
    position: absolute; left: 89px; top: 390px; width: 500px;
    font-weight: 300; font-size: 25.5px; line-height: 31px; color: var(--text-grey);
  }
  .benefits {
    position: absolute; left: 92px; top: 485px; list-style: none;
    font-weight: 400; font-size: 15px; line-height: 18.6px; color: var(--brand-green);
  }
  .mats-photo {
    position: absolute; left: -55px; top: 580px; width: 320px; height: 320px;
    border-radius: 50%;
    background: linear-gradient(90deg, var(--photo-floor) 0%, var(--mat-blue) 18%, var(--mat-blue) 42%, var(--mat-green) 48%, var(--mat-green) 78%, var(--photo-floor) 100%);
  }
  .venues {
    position: absolute; right: 36px; top: 580px; text-align: right;
  }
  .venues-heading {
    font-family: "Roboto Condensed", sans-serif; font-size: 23px; line-height: 1;
    color: var(--brand-blue); margin-bottom: 9px;
  }
  .venue {
    font-weight: 300; font-size: 14.5px; line-height: 18px; color: var(--text-dark);
    margin-bottom: 7px;
  }
  .contact {
    position: absolute; right: 38px; top: 742px; text-align: right;
    font-weight: 300; font-size: 21px; line-height: 25px; color: var(--brand-blue);
  }
  .cert-badge {
    position: absolute; left: 276px; top: 821px; width: 69px; height: 23px;
    background: #4e8fb0; border-radius: 2px;
  }
  .brand-name {
    position: absolute; left: 367px; top: 816px;
    font-weight: 300; font-size: 27px; line-height: 1; color: var(--brand-blue);
  }
</style>
</head>
<body>
  <main class="flyer">
    <div class="hero-photo" role="img" aria-label="Smiling class of men and women lying on blue mats in a bright studio, giving a thumbs up"></div>
    <div class="title-tab"></div>
    <div class="subtitle-tab"></div>
    <h1 class="title-script">Pilates</h1>
    <p class="title-sub">NEW CLASSES NEAR YOU!</p>

    <p class="intro">Pilates is for EVERYONE whatever level of fitness, age or ability to help you build strength, flexibility and overall well-being</p>

    <ul class="benefits">
      <li>Quality teaching with Balanced Motion Method Teacher</li>
      <li>Progressive approach.Teaching good movement skills</li>
      <li>Small class sizes and friendly atmosphere</li>
      <li>Beginners, Intermediate and Over 50’s classes to choose from</li>
    </ul>

    <div class="mats-photo" role="img" aria-label="Rolled blue and green exercise mats on a wooden floor"></div>

    <section class="venues">
      <h2 class="venues-heading">JOIN MY ONE-HOUR CLASSES AT</h2>
      <p class="venue">St Aldric’s Church Hall, Fern Rise<br>Monday evenings,Tuesday and Friday mornings</p>
      <p class="venue">Larkfield Meadows Dr.Surgery Tuesday evenings</p>
      <p class="venue">Penmore Centre,Kestrel Road,<br>Wednesday mornings and evenings</p>
    </section>

    <p class="contact">Call Wendy on 07700 900418<br>wendy.harlow@example.co.uk</p>

    <div class="cert-badge" role="img" aria-label="Teacher certification badge"></div>
    <p class="brand-name">Stillwater Pilates</p>
  </main>
</body>
</html>
```